Webdesign Bestattungswesen Quellbrück
Zielgruppe
Bestattungsunternehmen
Aufgabenstellung
- Seite soll keine Kopie der alten Webseite werden
- Logo muss unverändert bleiben
- KEIN schwarz als Hauptfarbe !
- sanfte Farben

```html
<!DOCTYPE html>
<html lang="de">
<head>
<meta charset="utf-8">
<title>Bestattungswesen Quellbrück</title>
<link href="https://fonts.googleapis.com/css2?family=Playfair+Display:wght@500;600&family=Poppins:wght@400;500;600&display=swap" rel="stylesheet">
<style>
:root{
  --bg:#f2f0eb;
  --gold:#d4a73a;
  --gold-soft:#ecd5a3;
  --ink:#4a3a10;
  --text:#6b6456;
  --white:#ffffff;
  --bar:#6f6a60;
}
*{margin:0;padding:0;box-sizing:border-box}
html,body{width:1200px;height:2584px;overflow:hidden}
body{background:var(--bg);font-family:'Poppins',sans-serif;color:var(--text);position:relative}
.abs{position:absolute}
.serif{font-family:'Playfair Display',serif;color:var(--ink);font-weight:500}
.pill{position:absolute;height:30px;border-radius:15px;background:var(--white);font-size:11px;font-weight:500;color:var(--ink);display:flex;align-items:center;padding:0 10px;gap:5px}
.phone-btn{position:absolute;height:30px;border-radius:15px;background:var(--gold);color:var(--ink);font-weight:600;font-size:13px;display:flex;align-items:center;gap:10px;padding:0 13px}
.phone-btn svg{width:20px;height:20px}
.brand{left:0;width:1200px;top:82px;text-align:center;font-size:24px}
.hero{left:88px;top:146px;width:1024px;height:312px;border-radius:30px;background:radial-gradient(circle at 33% 65%,#e6ebc8 0,transparent 30%),radial-gradient(circle at 70% 40%,#eef2dc 0,transparent 35%),linear-gradient(90deg,#dfe4e0,#f1f3ee 40%,#e4e9d6 75%,#e9efd1)}
.badge{position:absolute;top:362px;width:77px;height:77px;background:var(--white);border-radius:12px;display:flex;align-items:center;justify-content:center}
.badge span{width:46px;height:52px;border:1.5px solid #9c9c9c;border-radius:4px}
h1{position:absolute;left:0;width:1200px;top:498px;text-align:center;font-size:38px}
.intro{left:349px;top:606px;width:510px}
.intro h2{font-size:22px;margin-bottom:14px}
.intro p{font-size:13px;line-height:18.8px;margin-bottom:18.8px}
.claim{font-family:'Playfair Display',serif;color:var(--ink);font-weight:600;font-size:16px}
.kind{position:absolute;top:973px;width:330px;height:330px;border-radius:28px}
.kind h3{position:absolute;top:36px;width:100%;text-align:center;font-size:22px}
.kind .box{position:absolute;left:34px;top:83px;width:262px;height:214px;background:var(--white);border-radius:14px;text-align:center;font-size:13px;line-height:18.8px;padding:28px 30px 0}
.arrow{position:absolute;width:28px;height:28px;border-radius:50%;background:var(--gold-soft);display:flex;align-items:center;justify-content:center}
.arrow svg{width:14px;height:14px}
.service{position:absolute;top:1328px;width:330px;height:330px;background:var(--white);border-radius:28px;padding:32px 33px}
.service svg.ic{width:56px;height:56px}
.service h3{font-size:22px;margin:22px 0 10px}
.service p{font-size:13px;line-height:18.8px}
.faq-bg{left:0;top:1690px;width:1200px;height:530px;background:radial-gradient(ellipse 420px 300px at 330px 420px,#efbfae 0,rgba(240,200,180,.6) 45%,transparent 80%),radial-gradient(ellipse 300px 200px at 700px 500px,#eedcc4 0,transparent 70%)}
.faq-left{left:88px;top:1714px;width:420px}
.faq-left h2{font-size:22px;margin-bottom:14px}
.faq-left p{font-size:13px;line-height:18.8px}
.q{position:absolute;left:609px;width:503px;background:var(--white);border-radius:10px}
.q h4{position:absolute;left:20px;font-family:'Playfair Display',serif;color:var(--ink);font-weight:600;font-size:17px}
.q p{position:absolute;left:23px;top:52px;width:400px;font-size:13px;line-height:18.8px}
footer{position:absolute;left:0;top:2220px;width:1200px;height:304px;background:var(--white)}
.deco{left:0;top:2240px;width:320px;height:270px;background:radial-gradient(ellipse at 40% 55%,#f3e6cc 0,rgba(243,230,204,.4) 50%,transparent 75%)}
.addr{left:349px;top:2305px;font-size:13px;line-height:18.8px}
.addr strong{color:var(--ink);font-weight:600}
.contact{left:349px;display:flex;align-items:center;gap:14px;font-size:13px}
.contact svg{width:20px;height:20px}
.col{top:2290px;font-size:13px}
.col h5{font-family:'Playfair Display',serif;color:var(--ink);font-weight:600;font-size:17px;margin-bottom:10px}
.col a{display:block;color:var(--text);text-decoration:underline;line-height:25px}
.bottom{position:absolute;left:0;top:2524px;width:1200px;height:60px;background:var(--bar);color:var(--white);font-size:13px}
.bottom nav{position:absolute;left:89px;top:21px;display:flex;gap:25px}
.bottom .copy{position:absolute;right:88px;top:21px}
</style>
</head>
<body>
<svg width="0" height="0" style="position:absolute">
  <defs>
    <symbol id="phone" viewBox="0 0 24 24"><path d="M5 3h3.5l1.8 4.5-2.3 1.4a11 11 0 0 0 6.1 6.1l1.4-2.3L20 14.5V18a2 2 0 0 1-2 2A16 16 0 0 1 3 5a2 2 0 0 1 2-2z" fill="none" stroke="currentColor" stroke-width="1.6" stroke-linejoin="round"/></symbol>
    <symbol id="arr" viewBox="0 0 16 16"><path d="M2 8h11M9 4l4 4-4 4" fill="none" stroke="#4a3a10" stroke-width="1.5" stroke-linecap="round" stroke-linejoin="round"/></symbol>
  </defs>
</svg>

<header>
  <div class="pill" style="left:88px;top:37px">Bestattungsformen <svg width="9" height="9" viewBox="0 0 10 10"><path d="M2 3.5l3 3 3-3" fill="none" stroke="#4a3a10" stroke-width="1.2"/></svg></div>
  <div class="pill" style="left:235px;top:37px">Vorsorge</div>
  <div class="pill" style="left:316px;top:37px">Bestattungskosten</div>
  <div class="pill" style="left:778px;top:37px">Über uns</div>
  <div class="pill" style="left:858px;top:37px">Kontakt</div>
  <div class="abs" style="left:993px;top:14px;font-size:13px;color:var(--ink)">24h erreichbar</div>
  <div class="phone-btn" style="left:966px;top:35px"><svg style="color:var(--ink)"><use href="#phone"/></svg>03741 / 38 720</div>
  <div class="abs serif brand">Bestattungswesen Quellbrück</div>
</header>

<div class="abs hero" role="img" aria-label="Sanftes Blütenfoto in Weiß und Hellgrün"></div>
<div class="badge" style="left:760px"><span></span></div>
<div class="badge" style="left:843px"><span></span></div>
<div class="badge" style="left:927px"><span></span></div>
<div class="badge" style="left:1011px"><span></span></div>

<h1 class="serif">Bestattungswesen Quellbrück – Würdevolle Bestattungen</h1>

<section class="abs intro">
  <h2 class="serif">Bestattung und Vorsorge in besten Händen.</h2>
  <p>Eines Tages aber beschloß eine kleine Zeile Blindtext, ihr Name war Lorem Ipsum, hinaus zu gehen in die weite Grammatik. Der große Oxmox riet ihr davon ab, da es dort wimmele von bösen Kommata, wilden Fragezeichen und hinterhältigen Semikoli, doch das Blindtextchen ließ sich nicht beirren.</p>
  <p>Als es die ersten Hügel des Kursivgebirges erklommen hatte, warf es einen letzten Blick zurück auf die Skyline seiner Heimatstadt Buchstabhausen, die Headline von Alphabetdorf und die Subline seiner eigenen Straße, der Zeilengasse.</p>
  <div class="phone-btn" style="position:relative;display:inline-flex;margin-top:2px"><svg style="color:var(--ink)"><use href="#phone"/></svg>03741 / 38 720</div>
  <div class="claim" style="margin-top:14px">Wir sind 24 Stunden 365 Tage im Jahr erreichbar.</div>
</section>

<article class="kind" style="left:88px;background:linear-gradient(135deg,#f4b8a8,#f8dcd2 50%,#f3ccb8)" role="img" aria-label="Blütenfoto in Rosa und Pfirsich">
  <h3 class="serif">Feuerbestattung</h3>
  <div class="box">Es ist ein paradiesmatisches Land, in dem einem gebratene Satzteile in den Mund fliegen. Nicht einmal von der allmächtigen. Es packte seine sieben Versalien.
    <div class="arrow" style="left:213px;top:161px"><svg><use href="#arr"/></svg></div></div>
</article>
<article class="kind" style="left:435px;background:linear-gradient(135deg,#e2dcdc,#f0d6c8 50%,#e8c8c0)" role="img" aria-label="Blütenfoto in Beige und Altrosa">
  <h3 class="serif">Erdbestattung</h3>
  <div class="box">Es ist ein paradiesmatisches Land, in dem einem gebratene Satzteile in den Mund fliegen. Nicht einmal von der allmächtigen. Es packte seine sieben Versalien.
    <div class="arrow" style="left:213px;top:161px"><svg><use href="#arr"/></svg></div></div>
</article>
<article class="kind" style="left:783px;background:linear-gradient(135deg,#cbc4d4,#e6e0e6 50%,#e3d8e2)" role="img" aria-label="Blütenfoto in Flieder und Grau">
  <h3 class="serif">Seebestattung</h3>
  <div class="box">Es ist ein paradiesmatisches Land, in dem einem gebratene Satzteile in den Mund fliegen. Nicht einmal von der allmächtigen. Es packte seine sieben Versalien.
    <div class="arrow" style="left:213px;top:161px"><svg><use href="#arr"/></svg></div></div>
</article>

<article class="service" style="left:88px">
  <svg class="ic" viewBox="0 0 56 56" fill="none" stroke="#ecd5a3" stroke-width="3" stroke-linejoin="round"><path d="M12 4h30M12 52h30M16 4c0 14 20 14 20 24S16 38 16 52M38 4c0 14-20 14-20 24s20 10 20 24"/></svg>
  <h3 class="serif">Bestattungsvorsorge</h3>
  <p>Es ist ein paradiesmatisches Land, in dem einem gebratene Satzteile in den Mund fliegen. Nicht einmal von der allmächtigen. Es packte seine sieben Versalien.</p>
  <div class="arrow" style="left:273px;top:275px"><svg><use href="#arr"/></svg></div>
</article>
<article class="service" style="left:435px">
  <svg class="ic" viewBox="0 0 56 56" fill="none" stroke="#ecd5a3" stroke-width="3" stroke-linejoin="round"><path d="M10 20c4-8 14-10 22-9l6-5v8c4 2 7 6 8 10h4v10h-5c-2 4-5 6-7 7v7h-7v-5h-9v5h-7v-8c-5-4-8-11-5-20z"/><circle cx="44" cy="14" r="7"/></svg>
  <h3 class="serif">Bestattungskosten</h3>
  <p>Es ist ein paradiesmatisches Land, in dem einem gebratene Satzteile in den Mund fliegen. Nicht einmal von der allmächtigen.</p>
  <div class="arrow" style="left:273px;top:275px"><svg><use href="#arr"/></svg></div>
</article>
<article class="service" style="left:783px">
  <svg class="ic" viewBox="0 0 56 56" fill="none" stroke="#ecd5a3" stroke-width="3"><circle cx="28" cy="28" r="25"/><ellipse cx="28" cy="28" rx="11" ry="25"/><path d="M3 28h50M7 15h42M7 41h42M28 3v50"/></svg>
  <h3 class="serif">Überführungen</h3>
  <p>Es ist ein paradiesmatisches Land, in dem einem gebratene Satzteile in den Mund fliegen. Nicht einmal von der allmächtigen. Es packte seine sieben Versalien.</p>
  <div class="arrow" style="left:273px;top:275px"><svg><use href="#arr"/></svg></div>
</article>

<div class="abs faq-bg"></div>
<section class="abs faq-left">
  <h2 class="serif">Häufig gestellte Fragen</h2>
  <p>Es ist ein paradiesmatisches Land, in dem einem gebratene Satzteile in den Mund fliegen. Nicht einmal von der allmächtigen. Es packte seine sieben Versalien.</p>
  <div class="phone-btn" style="position:relative;display:inline-flex;margin-top:22px"><svg style="color:var(--ink)"><use href="#phone"/></svg>03741 / 38 720</div>
  <div class="claim" style="margin-top:14px">Wir sind rund um die Uhr für Sie da.</div>
</section>

<div class="q" style="top:1715px;height:163px">
  <h4 style="top:16px">Lorem ipsum dolor sit amet consectetur?</h4>
  <div class="arrow" style="left:448px;top:16px"><svg viewBox="0 0 16 16"><path d="M4 10l4-4 4 4" fill="none" stroke="#4a3a10" stroke-width="1.5"/></svg></div>
  <p>Eine wunderbare Heiterkeit hat meine ganze Seele eingenommen, gleich den süßen Frühlingsmorgen, die ich mit ganzem Herzen genieße. Ich bin allein und freue mich meines Lebens in dieser Gegend, die für solche Seelen geschaffen ist wie die meine.</p>
</div>
<div class="q" style="top:1893px;height:55px"><h4 style="top:15px">Lorem ipsum dolor sit amet consectetur adipiscing?</h4><div class="arrow" style="left:448px;top:14px"><svg viewBox="0 0 16 16"><path d="M4 6l4 4 4-4" fill="none" stroke="#4a3a10" stroke-width="1.5"/></svg></div></div>
<div class="q" style="top:1963px;height:55px"><h4 style="top:15px">Lorem ipsum dolor sit amet?</h4><div class="arrow" style="left:448px;top:14px"><svg viewBox="0 0 16 16"><path d="M4 6l4 4 4-4" fill="none" stroke="#4a3a10" stroke-width="1.5"/></svg></div></div>
<div class="q" style="top:2034px;height:55px"><h4 style="top:15px">Lorem ipsum dolor sit amet?</h4><div class="arrow" style="left:448px;top:14px"><svg viewBox="0 0 16 16"><path d="M4 6l4 4 4-4" fill="none" stroke="#4a3a10" stroke-width="1.5"/></svg></div></div>
<div class="q" style="top:2104px;height:55px"><h4 style="top:15px">Lorem ipsum dolor sit amet consectetur adipiscing?</h4><div class="arrow" style="left:448px;top:14px"><svg viewBox="0 0 16 16"><path d="M4 6l4 4 4-4" fill="none" stroke="#4a3a10" stroke-width="1.5"/></svg></div></div>

<footer></footer>
<div class="abs deco" role="img" aria-label="Dezente helle Farbfläche als Dekoration"></div>
<address class="abs addr" style="font-style:normal"><strong>Bestattungswesen Quellbrück</strong><br>Inhaberin Helene Marwitz<br>Lindenweg 14<br>09517 Quellbrück</address>
<div class="abs contact" style="top:2420px"><svg style="color:var(--text)"><use href="#phone"/></svg>03741 / 38 720</div>
<div class="abs contact" style="top:2451px"><svg viewBox="0 0 24 24" fill="none" stroke="#6b6456" stroke-width="1.6"><rect x="3" y="5" width="18" height="14" rx="2"/><path d="M3 7l9 6 9-6"/></svg>info@bestattungswesen-quellbrueck.de</div>
<nav class="abs col" style="left:695px"><h5>Bestattungsarten</h5><a>Baumbestattung</a><a>Erdbestattung</a><a>Seebestattung</a><a>Feuerbestattung</a><a>Anonyme Bestattung</a><a>Besondere Bestattungen</a></nav>
<nav class="abs col" style="left:908px"><h5>Im Trauerfall</h5><a>Erste Schritte</a><a>Leistungen</a><a>Friedhöfe</a><a>Floristik</a><a>Trauerdruck</a><a>Bestattungskosten</a></nav>

<div class="bottom">
  <nav><span>Startseite</span><span>Sitemap</span><span>Datenschutz</span><span>Impressum</span></nav>
  <div class="copy">© Bestattungswesen Quellbrück - All Rights Reserved</div>
</div>
</body>
</html>
```